Barristers Chambers - Letterhead and Logo amendments

Brisdane Chambers is a barristers chambers in Marrowby Rise, just around the corner from st. Olvens cathedral. We already have the logo and colour scheme but I think it can be improved, possibly with a better lettermark? we also have a small square version of it.
Main brand colour is: 671E75 – Purple.
Slogan: CONNECTING BARRISTERS, SOLICITORS AND OTHER PROFESSIONALS
I will attach both logos and also our current letterhead, which we made ourselves but it doesn't look professional enough.
Name of the Chambers: Brisdane Chambers
Tagline/Slogan (if any): None
Design Elements:
The logo should be simple and easy to recognize.
It should reflect the nature of the Chambers' work and be relevant to the legal industry.
Any images or graphics used should be unique, professional, and not overly complex.
The logo should be adaptable to various media, such as business cards, letterheads, and digital marketing materials.
It should be legible and easy to read, even when used at a small size.
The colour scheme should be professional and reflect the Chambers' brand identity.
Target Market(s)
Solicitors, lawyers and business clients
Industry/Entity Type
Legal

```html
<!DOCTYPE html>
<html lang="en">
<head>
<meta charset="utf-8">
<title>Brisdane Chambers – Letterhead</title>
<link href="https://fonts.googleapis.com/css2?family=Mulish:ital,wght@0,400;0,600;0,700;1,400;1,700&display=swap" rel="stylesheet">
<style>
  :root {
    --brand-purple: #671e75;
    --backdrop: #b9c3d3;
    --paper: #ffffff;
    --body-grey: #6f6f73;
    --ink: #1f1f22;
    --signature-tone: #ececef;
  }
  * { box-sizing: border-box; margin: 0; padding: 0; }
  html, body {
    width: 1200px; height: 900px; overflow: hidden;
    background: var(--backdrop);
    font-family: "Mulish", sans-serif;
  }
  .letterhead {
    position: absolute; left: 296px; top: 20px;
    width: 608px; height: 860px;
    background: var(--paper);
    box-shadow: 0 10px 30px rgba(40, 50, 70, 0.25);
    overflow: hidden;
  }
  .letterhead__footer-band {
    position: absolute; left: 0; right: 0; bottom: 0;
    height: 14px; background: var(--brand-purple);
  }
  .masthead {
    position: absolute; left: 60px; right: 46px; top: 66px;
    display: flex; justify-content: space-between; align-items: center;
  }
  .brand__name {
    color: var(--brand-purple); font-weight: 600;
    font-size: 18px; line-height: 1.05; letter-spacing: 0.06em;
  }
  .contact { display: flex; align-items: stretch; gap: 9px; font-size: 6.8px; color: var(--ink); font-style: italic; }
  .contact__address { text-align: right; line-height: 1.6; font-style: italic; }
  .contact__address strong { font-weight: 700; }
  .contact__divider { width: 1px; background: var(--brand-purple); }
  .contact__lines { list-style: none; line-height: 1.6; }
  .contact__lines li { display: flex; align-items: center; gap: 4px; }
  .contact__lines svg { width: 6px; height: 6px; fill: none; stroke: var(--brand-purple); stroke-width: 1.4; }
  .letter {
    position: absolute; left: 72px; right: 56px; top: 190px;
    color: var(--body-grey); font-weight: 400;
    font-size: 11.2px; line-height: 19px;
  }
  .letter__salutation { margin-bottom: 26px; font-size: 11.5px; }
  .letter__paragraph { margin-bottom: 17px; text-align: justify; }
  .signature {
    position: absolute; left: 72px; top: 612px;
    width: 150px; height: 56px; background: var(--signature-tone);
  }
</style>
</head>
<body>
  <article class="letterhead">
    <header class="masthead">
      <div class="brand">
        <div class="brand__name">BRISDANE<br>CHAMBERS</div>
      </div>
      <div class="contact">
        <address class="contact__address">
          <strong>Brisdane Chambers</strong><br>
          Suite 4, 12 Marrowby Rise<br>
          London EC9Z 4QX
        </address>
        <span class="contact__divider"></span>
        <ul class="contact__lines">
          <li><svg viewBox="0 0 10 10"><path d="M2 1 L4 3 L3 4.5 Q4.5 6.5 5.5 7 L7 6 L9 8 L7.5 9.5 Q2 8 0.5 2.5 Z"/></svg>01632 960418</li>
          <li><svg viewBox="0 0 10 10"><rect x="1" y="2.5" width="8" height="5.5"/><path d="M1 2.5 L5 5.5 L9 2.5"/></svg>contact@brisdanechambers.co.uk</li>
          <li><svg viewBox="0 0 10 10"><circle cx="5" cy="5" r="4"/><path d="M1 5 H9 M5 1 Q2.5 5 5 9 M5 1 Q7.5 5 5 9"/></svg>www.brisdanechambers.co.uk</li>
        </ul>
      </div>
    </header>

    <section class="letter">
      <p class="letter__salutation">Dear Edwin,</p>
      <p class="letter__paragraph">Lorem Ipsum is simply dummy text of the printing and typesetting industry. Lorem Ipsum has been the industry's standard dummy text ever since the 1500s, when an unknown printer took a galley of type and scrambled it to make a type specimen book. It has survived not only five centuries, but also the leap into electronic typesetting, remaining essentially unchanged. It was popularised in the 1960s with the release of Pressline sheets containing Lorem Ipsum passages, and more recently with desktop publishing software like Folioset Composer including versions of Lorem Ipsum.</p>
      <p class="letter__paragraph">Lorem Ipsum is simply dummy text of the printing and typesetting industry. Lorem Ipsum has been the industry's standard dummy text ever since the 1500s, when an unknown printer took a galley of type and scrambled it to make a type specimen book.</p>
      <p class="letter__paragraph">Lorem Ipsum is simply dummy text of the printing and typesetting industry. Lorem Ipsum has been the industry's standard dummy text ever since the 1500s, when an unknown printer took a galley of type and scrambled it to make a type specimen book. It has survived not only five centuries, but also the leap into electronic typesetting, remaining essentially unchanged. It was popularised in the 1960s with the release of Pressline sheets containing Lorem Ipsum passages,</p>
    </section>

    <div class="signature" role="img" aria-label="Handwritten signature of the sender"></div>

    <div class="letterhead__footer-band"></div>
  </article>
</body>
</html>
```